Business Card Design Project

i need a bussines car design
Veltra Clinical Hypnotherapy

Gordon Wexley
Psychotherapy & Hypnosis

64029381 /0427956120

back of the card appoinment space.

file was provided on a PDF, LOgo , use the blu colorsa as well , elegant, clear,

Target Market(s)

young professional, caucasian , young mothers.

Industry/Entity Type

Business

```html
<!DOCTYPE html>
<html lang="en">
<head>
<meta charset="utf-8">
<title>Veltra Clinical Hypnotherapy – Business Card</title>
<link rel="stylesheet" href="https://fonts.googleapis.com/css2?family=Lato:wght@300;400;700&family=Questrial&display=swap">
<style>
  :root {
    --bg: #a6a8ab;
    --ink-black: #141414;
    --band-black: #1b1b1b;
    --brand-blue: #1ea2dc;
    --name-blue: #33aee6;
    --shadow-blue: #0f6f99;
    --paper: #ffffff;
    --text-dark: #2a2a2a;
    --text-light: #ffffff;
    --muted: #d9d9d9;
  }
  * { box-sizing: border-box; margin: 0; padding: 0; }
  html, body { width: 1200px; height: 1000px; overflow: hidden; }
  body {
    background: var(--bg);
    font-family: "Lato", Arial, sans-serif;
    display: flex;
    align-items: center;
    justify-content: center;
    gap: 40px;
  }
  .card {
    position: relative;
    width: 540px;
    height: 324px;
    overflow: hidden;
    box-shadow: 0 6px 14px rgba(0,0,0,0.35);
  }

  /* Front */
  .card-front { background: var(--brand-blue); }
  .front-header {
    position: absolute; inset: 0 0 auto 0;
    height: 53px;
    background: var(--ink-black);
    display: flex; align-items: center; justify-content: center;
    z-index: 2;
  }
  .holder-name {
    font-family: "Questrial", Arial, sans-serif;
    font-weight: 400;
    color: var(--name-blue);
    font-size: 29px;
    letter-spacing: 0.5px;
    text-transform: uppercase;
  }
  .header-shade {
    position: absolute; top: 53px; left: 0; right: 0; height: 14px;
    background: linear-gradient(var(--shadow-blue), var(--brand-blue));
    z-index: 1;
  }
  .portrait {
    position: absolute; left: 0; top: 53px;
    width: 285px; height: 175px;
    background: radial-gradient(ellipse at 50% 35%, #c8906c 0%, #b98060 28%, #efe4cf 62%, #e6d9bf 100%);
  }
  .phone-line {
    position: absolute; right: 22px; top: 140px;
    display: flex; align-items: center; gap: 9px;
    color: var(--text-light);
    font-size: 16px;
    white-space: nowrap;
  }
  .phone-icon {
    width: 22px; height: 22px;
    background: var(--ink-black);
    border-radius: 3px;
    display: flex; align-items: center; justify-content: center;
  }
  .front-footer {
    position: absolute; left: 0; right: 0; bottom: 0;
    height: 96px;
    background: var(--ink-black);
  }
  .brand-name {
    position: absolute; left: 140px; top: 18px;
    font-family: "Questrial", Arial, sans-serif;
    font-size: 30px;
    color: var(--brand-blue);
    white-space: nowrap;
  }
  .brand-web {
    position: absolute; left: 140px; top: 60px;
    font-size: 14px;
    color: var(--muted);
    white-space: nowrap;
  }
  .member-badge {
    position: absolute; right: 26px; top: 20px;
    width: 56px; height: 56px; border-radius: 50%;
    background: radial-gradient(circle, #f2d22a 0%, #8cc43c 70%, #2f7f3a 100%);
    border: 2px solid #ffffff;
  }

  /* Back */
  .card-back { background: var(--paper); }
  .back-header {
    height: 62px;
    background: var(--band-black);
    display: flex; align-items: center; justify-content: center;
    color: var(--text-light);
    font-size: 19px;
    letter-spacing: 2.5px;
  }
  .back-header strong { font-weight: 700; margin-right: 8px; letter-spacing: 3px; }
  .appointments {
    list-style: none;
    padding: 2px 0 0 26px;
  }
  .appointment {
    display: flex; align-items: flex-end;
    height: 37.5px;
    font-size: 15px;
    color: var(--text-dark);
    white-space: nowrap;
  }
  .slot-no { width: 18px; }
  .blank { display: inline-block; border-bottom: 1px solid var(--text-dark); height: 16px; }
  .blank-time { width: 44px; margin-right: 8px; }
  .blank-name { width: 180px; margin: 0 6px 0 8px; }
  .blank-d { width: 34px; }
  .sep { margin: 0 2px; }
  .back-footer {
    position: absolute; left: 0; right: 0; bottom: 0;
    height: 52px;
    background: var(--band-black);
    color: var(--text-light);
    font-size: 13px;
    text-align: center;
    display: flex; flex-direction: column; justify-content: center;
    line-height: 1.45;
  }
</style>
</head>
<body>

  <section class="card card-front" aria-label="Card front">
    <header class="front-header">
      <h1 class="holder-name">Gordon Wexley</h1>
    </header>
    <div class="header-shade"></div>
    <div class="portrait" role="img" aria-label="Portrait photo of the therapist"></div>
    <p class="phone-line">
      <span>64029381 /0427956120</span>
      <span class="phone-icon">
        <svg width="13" height="13" viewBox="0 0 24 24" aria-hidden="true">
          <path d="M6.6 10.8a15.1 15.1 0 0 0 6.6 6.6l2.2-2.2a1 1 0 0 1 1-.25 11.4 11.4 0 0 0 3.6.57 1 1 0 0 1 1 1V20a1 1 0 0 1-1 1A17 17 0 0 1 3 4a1 1 0 0 1 1-1h3.5a1 1 0 0 1 1 1c0 1.25.2 2.45.57 3.57a1 1 0 0 1-.25 1z" fill="#ffffff"/>
        </svg>
      </span>
    </p>
    <footer class="front-footer">
      <p class="brand-name">Veltra Hypnotherapy</p>
      <p class="brand-web">www.veltraclinicalhypnotherapy.com.au</p>
      <div class="member-badge" role="img" aria-label="Professional association badge"></div>
    </footer>
  </section>

  <section class="card card-back" aria-label="Card back">
    <header class="back-header"><strong>VELTRA</strong> Clinical Hypnotherapy</header>
    <ol class="appointments">
      <li class="appointment"><span class="slot-no">1</span><span class="blank blank-time"></span>am/pm<span class="blank blank-name"></span><span class="blank blank-d"></span><span class="sep">/</span><span class="blank blank-d"></span><span class="sep">/</span><span class="blank blank-d"></span></li>
      <li class="appointment"><span class="slot-no">2</span><span class="blank blank-time"></span>am/pm<span class="blank blank-name"></span><span class="blank blank-d"></span><span class="sep">/</span><span class="blank blank-d"></span><span class="sep">/</span><span class="blank blank-d"></span></li>
      <li class="appointment"><span class="slot-no">3</span><span class="blank blank-time"></span>am/pm<span class="blank blank-name"></span><span class="blank blank-d"></span><span class="sep">/</span><span class="blank blank-d"></span><span class="sep">/</span><span class="blank blank-d"></span></li>
      <li class="appointment"><span class="slot-no">4</span><span class="blank blank-time"></span>am/pm<span class="blank blank-name"></span><span class="blank blank-d"></span><span class="sep">/</span><span class="blank blank-d"></span><span class="sep">/</span><span class="blank blank-d"></span></li>
      <li class="appointment"><span class="slot-no">5</span><span class="blank blank-time"></span>am/pm<span class="blank blank-name"></span><span class="blank blank-d"></span><span class="sep">/</span><span class="blank blank-d"></span><span class="sep">/</span><span class="blank blank-d"></span></li>
    </ol>
    <footer class="back-footer">
      <p>By Appointment&nbsp; Phone: 0427 956 120 | 184 Harlow Street, Kensington 3031</p>
      <p>gordon@veltraclinicalhypnotherapy.com.au</p>
    </footer>
  </section>

</body>
</html>
```